Kelvane Plumbing Business cards

Company is Kelvane Plumbing.
name Dashel Morrowby, I am a plumber, drainer, gasfitter and roofer
Mobile: 0431 906 154
Email address: info@kelvaneplumbing.example (check out my website for some ideas)
Website: www.kelvaneplumbing.example
ABN: 82 916 203 471
LIC: 604517K

I am reliable all round plumber. I am a 24 hour emergency service. Kelvane Plumbing is a professional plumbing service in the Illawarra, South Coast, Southern Sydney and Southern Highland regions of NSW. We offer a 24 hour emergency service for piece of mind to our customers. Call us now to see how we can help you. Kelvane Plumbing approaches every job with attention to detail and excellent customer service. With our superior workmanship you can be confident that the job will be done right the first time around. You can rest assured with results that are guaranteed to last.

Target Market(s)

the general public

Contact Information for Business Card

look up website for some ideas something with similar colours to logo and new modern and to catch the eye.

Colors
fdfdfd
ffffff
000000
7f7f7f
aaaaaa
33a6d7
0492cd

Requirements
Must have
• all contact details
• company- Kelvane Plumbing
• name- Dashel Morrowby
• number mobile- 0431 906 154
• Email address- info@kelvaneplumbing.example
• Website- www.kelvaneplumbing.example
• ABN- 82 916 203 471
• LIC- 604517K

```html
<!DOCTYPE html>
<html lang="en">
<head>
<meta charset="utf-8">
<title>Kelvane Plumbing — Business Cards</title>
<link href="https://fonts.googleapis.com/css2?family=Source+Sans+3:wght@400;600;700&display=swap" rel="stylesheet">
<style>
  :root {
    --brand-blue: #0492cd;
    --brand-blue-light: #33a6d7;
    --ink: #000000;
    --band: #121212;
    --paper: #fdfdfd;
    --white: #ffffff;
    --grey: #7f7f7f;
    --text-dark: #333333;
    --backdrop: #e6e6e6;
  }
  * { margin: 0; padding: 0; box-sizing: border-box; }
  html, body { width: 1200px; height: 1200px; overflow: hidden; }
  body {
    background: var(--backdrop);
    font-family: "Source Sans 3", "Myriad Pro", sans-serif;
    position: relative;
  }
  .card {
    position: absolute;
    width: 940px;
    height: 564px;
    background: var(--paper);
    overflow: hidden;
    box-shadow: 0 6px 18px rgba(0,0,0,0.18);
  }
  /* ---------- front ---------- */
  .card--front { left: 29px; top: 21px; }
  .front__brand {
    position: absolute; left: 0; top: 0;
    width: 529px; height: 100%;
    background: var(--brand-blue);
  }
  .brand-mark {
    position: absolute; left: 192px; top: 165px;
    width: 144px; height: 144px;
    border: 9px solid var(--white);
    border-radius: 50%;
  }
  .front__company {
    position: absolute; left: 0; width: 100%; top: 355px;
    text-align: center;
    color: var(--white);
    font-weight: 700;
    font-size: 30px;
    letter-spacing: 2px;
  }
  .front__person { position: absolute; left: 592px; top: 99px; }
  .person__name {
    color: var(--brand-blue);
    font-weight: 600;
    font-size: 33px;
    line-height: 1;
  }
  .person__role {
    margin-top: 14px;
    color: var(--text-dark);
    font-size: 20px;
    letter-spacing: 5px;
  }
  .rule {
    position: absolute; left: 592px; width: 254px; height: 4px;
    background: var(--brand-blue);
  }
  .rule--top { top: 191px; }
  .rule--bottom { top: 369px; }
  .contact-band {
    position: absolute; left: 529px; right: 0; top: 195px; height: 174px;
    background: var(--band);
  }
  .contact-list { list-style: none; position: absolute; left: 63px; top: 26px; }
  .contact-list li {
    display: flex; align-items: center;
    height: 44px;
    color: var(--white);
    font-size: 20px;
  }
  .contact-list svg { width: 36px; height: 36px; margin-right: 17px; flex: none; }
  .registration {
    position: absolute; left: 592px; top: 385px;
    color: var(--text-dark);
    font-size: 20px;
    line-height: 30px;
  }
  .registration b { color: var(--brand-blue); font-weight: 600; display: inline-block; width: 44px; }
  /* ---------- back ---------- */
  .card--back { left: 212px; top: 610px; background: var(--white); }
  .back__mark {
    position: absolute; left: 90px; top: 212px;
    width: 140px; height: 140px;
    border: 9px solid var(--brand-blue);
    border-radius: 50%;
  }
  .back__company {
    position: absolute; left: 257px; top: 260px;
    color: var(--ink);
    font-size: 34px;
    font-weight: 600;
    letter-spacing: -0.5px;
    line-height: 1;
  }
  .back__web {
    position: absolute; left: 572px; right: 0; top: 249px; height: 66px;
    background: var(--brand-blue);
    color: var(--white);
    font-size: 22px;
    display: flex; align-items: center; justify-content: center;
  }
</style>
</head>
<body>

<section class="card card--front">
  <div class="front__brand">
    <div class="brand-mark" aria-hidden="true"></div>
    <div class="front__company">Kelvane Plumbing</div>
  </div>

  <div class="front__person">
    <div class="person__name">Dashel Morrowby</div>
    <div class="person__role">Plumber</div>
  </div>

  <div class="rule rule--top"></div>
  <div class="contact-band">
    <ul class="contact-list">
      <li>
        <svg viewBox="0 0 36 36" aria-hidden="true">
          <circle cx="18" cy="18" r="16" fill="none" stroke="#0492cd" stroke-width="2.5"/>
          <path d="M10 14c0-3 16-3 16 0v2h-4v-2h-8v2h-4z" fill="#fff"/>
          <path d="M12 17h12l2 7H10z" fill="#fff"/>
          <circle cx="18" cy="20.5" r="2" fill="#121212"/>
        </svg>0431 906 154
      </li>
      <li>
        <svg viewBox="0 0 36 36" aria-hidden="true">
          <circle cx="18" cy="18" r="16" fill="none" stroke="#0492cd" stroke-width="2.5"/>
          <rect x="9" y="12" width="18" height="12" fill="#fff"/>
          <path d="M9 12l9 7 9-7M9 24l7-6M27 24l-7-6" fill="none" stroke="#121212" stroke-width="1.3"/>
        </svg>info@kelvaneplumbing.example
      </li>
      <li>
        <svg viewBox="0 0 36 36" aria-hidden="true">
          <circle cx="18" cy="18" r="16" fill="none" stroke="#0492cd" stroke-width="2.5"/>
          <g fill="none" stroke="#fff" stroke-width="1.5">
            <circle cx="18" cy="18" r="9"/>
            <ellipse cx="18" cy="18" rx="4" ry="9"/>
            <path d="M9 18h18M10.5 13.5h15M10.5 22.5h15M18 9v18"/>
          </g>
        </svg>www.kelvaneplumbing.example
      </li>
    </ul>
  </div>
  <div class="rule rule--bottom"></div>

  <div class="registration">
    <div><b>ABN</b>- 82 916 203 471</div>
    <div><b>LIC</b>- 604517K</div>
  </div>
</section>

<section class="card card--back">
  <div class="back__mark" aria-hidden="true"></div>
  <div class="back__company">KELVANE PLUMBING</div>
  <div class="back__web">www.kelvaneplumbing.example</div>
</section>

</body>
</html>
```